Harlow Solutions Website

My business has been word of mouth over the last 3 years and has grown. Now I need a website for additional marketing as we have new clients asking for a website.

You have already completed my Logo during an earlier project. I have attached the logo.

We do Staff Augmentation and Operation Support.

What is that?
Staff augmentation is an outsourcing strategy that allows companies to fill specific, temporary roles to achieve business objectives. This staffing method complements existing teams with specific talent, enhancing business capabilities or filling gaps left by members on extended leave.

We work alongside the internal recruiting team to assist clients to meet and exceed financial goals.

```html
<!DOCTYPE html>
<html lang="en">
<head>
<meta charset="utf-8">
<title>Harlow Solutions — Staff Augmentation</title>
<link href="https://fonts.googleapis.com/css2?family=Outfit:wght@300;400;500;600;700&display=swap" rel="stylesheet">
<style>
:root{
  --navy:#0d4d75;
  --navy-dark:#0a3d5e;
  --ink:#1d2633;
  --text:#5b6470;
  --muted:#8a929c;
  --band:#2f6e94;
  --band-dark:#1f5778;
  --card-pink:#fcefee;
  --soft:#f5f5f6;
  --line:#d9dde2;
  --footer:#0f1b28;
  --curve:#8c8c8c;
  --white:#ffffff;
}
*{box-sizing:border-box;margin:0;padding:0}
html,body{width:1200px;height:3692px;overflow:hidden;background:var(--white)}
body{font-family:'Outfit',sans-serif;color:var(--ink);position:relative}
.abs{position:absolute}
a{color:inherit;text-decoration:none}

/* header */
.site-header{left:0;top:0;width:1200px;height:72px;background:var(--white);z-index:5}
.brand{display:flex;align-items:center;gap:10px}
.brand-dot{width:40px;height:40px;border-radius:50%;background:var(--navy)}
.brand-name{color:var(--navy);font-weight:600;line-height:1}
.site-header .brand{left:118px;top:14px}
.site-header .brand-name{font-size:24px}
.site-header .brand-name small{display:block;font-size:13px;letter-spacing:.5px;margin-top:2px}
.main-nav{left:494px;top:26px;display:flex;gap:0;font-size:15px;color:#3a4350}
.main-nav a{position:absolute;white-space:nowrap}
.main-nav .active{color:var(--navy);font-weight:500}
.main-nav .active::after{content:"";position:absolute;left:-3px;right:-3px;top:24px;height:2px;background:var(--navy)}
.nav-divider{left:910px;top:22px;width:1px;height:26px;background:var(--line)}
.phone-pill{left:937px;top:19px;width:144px;height:32px;border:1.5px solid #9aa3ad;border-radius:16px;display:flex;align-items:center;justify-content:center;gap:8px;font-size:14px;color:#2b3440}

/* hero */
.hero-photo{left:0;top:72px;width:1200px;height:640px;background:linear-gradient(120deg,#3f4f5c 0%,#8a7a5e 35%,#c2a277 55%,#6d6a61 75%,#2c3a46 100%)}
.hero-shade{left:0;top:72px;width:1200px;height:640px;background:rgba(10,25,40,.28)}
.hero-curve{left:0;top:600px;width:1200px;height:130px}
.hero-title{left:0;top:262px;width:1200px;text-align:center;color:var(--white);font-size:47px;font-weight:600;letter-spacing:-.3px}
.hero-sub{left:0;top:331px;width:1200px;text-align:center;color:var(--white);font-size:19px;font-weight:300}
.btn{display:inline-flex;align-items:center;justify-content:center;font-weight:500;text-transform:uppercase;font-size:13px}
.hero-btn{left:536px;top:380px;width:128px;height:33px;border-radius:17px;background:var(--navy);color:var(--white);font-size:14px}

/* feature cards */
.feature{width:238px;height:337px;top:621px;background:var(--white);border-radius:6px;box-shadow:0 4px 18px rgba(0,0,0,.08);text-align:center;z-index:3}
.feature.is-featured{background:var(--navy);color:var(--white);box-shadow:0 10px 24px rgba(13,77,117,.35)}
.feature svg{position:absolute;left:84px;top:36px}
.feature h3{position:absolute;top:154px;width:100%;font-size:17px;font-weight:500;text-transform:uppercase}
.feature p{position:absolute;top:186px;left:20px;width:198px;font-size:12px;line-height:20px;color:var(--text)}
.feature.is-featured p{color:#dfe9f1}
.feature .btn{position:absolute;left:58px;top:268px;width:123px;height:36px;border:1.5px solid var(--line);border-radius:4px;color:var(--navy);background:var(--white)}

/* about */
.about-title{left:196px;top:1106px;font-size:31px;font-weight:500;line-height:41px;color:var(--ink)}
.about-copy{left:196px;top:1202px;width:380px;font-size:11px;line-height:24px;color:var(--text)}
.about-btn{left:194px;top:1342px;width:123px;height:35px;border-radius:4px;background:var(--navy);color:var(--white)}
.about-bg{left:748px;top:1046px;width:310px;height:310px;border-radius:50%;background:#f5f5fb}
.about-photo{left:680px;top:1062px;width:320px;height:372px;border-radius:50%;background:linear-gradient(150deg,#d5c8b8 0%,#8b8f94 45%,#3e4650 100%)}

/* services */
.testimonial-bg{left:0;top:2300px;width:1200px;height:561px;background:var(--soft)}
.services-band{left:0;top:1420px;width:1200px;height:1100px}
.services-title{left:0;top:1636px;width:1200px;text-align:center;color:var(--white);font-size:43px;font-weight:500}
.services-sub{left:0;top:1698px;width:1200px;text-align:center;color:var(--white);font-size:15px;line-height:23px;font-weight:300}
.service{width:244px;height:214px;background:var(--card-pink);text-align:center}
.service svg{position:absolute;left:92px;top:36px}
.service h4{position:absolute;top:124px;width:100%;font-size:15px;font-weight:500;color:var(--ink)}
.service p{position:absolute;top:148px;left:24px;width:196px;font-size:10px;line-height:16px;color:var(--muted)}

/* testimonials */
.quote{background:var(--white);padding:22px 28px 22px 56px;font-size:11.5px;line-height:21px;color:var(--text)}
.quote::before{content:"\201C";position:absolute;left:22px;top:10px;font-size:44px;color:var(--navy);font-weight:700;line-height:1}
.quote::after{content:"";position:absolute;left:30px;bottom:-10px;border-left:10px solid transparent;border-right:10px solid transparent;border-top:10px solid var(--white)}
.avatar{width:44px;height:44px;border-radius:50%;background:linear-gradient(135deg,#b9bec4,#5e6670)}
.person-name{font-size:11px;font-weight:600;letter-spacing:.4px;text-transform:uppercase;color:var(--ink)}
.person-role{font-size:10px;color:var(--muted);margin-top:4px}
.dots{left:584px;top:2788px;display:flex;gap:4px}
.dots span{width:7px;height:7px;border-radius:50%;border:1px solid var(--navy)}
.dots span.on{background:var(--navy)}

/* contact */
.contact-title{left:0;top:2918px;width:1200px;text-align:center;font-size:33px;font-weight:700;color:#1a1f26}
.contact-sub{left:0;top:2962px;width:1200px;text-align:center;font-size:14px;line-height:21px;color:#3a4350}
.footer-bg{left:0;top:3190px;width:1200px;height:502px}
.contact-card{left:194px;top:3029px;width:813px;height:301px;background:var(--white);border-top:3px solid var(--navy);box-shadow:0 6px 20px rgba(0,0,0,.08)}
.contact-card h2{position:absolute;left:90px;top:24px;font-size:19px;font-weight:400;color:#2b3440}
.field{position:absolute;border:1px solid var(--line);border-radius:3px;font-size:10px;color:#9aa1a9;padding:8px 14px}
.submit{position:absolute;left:90px;top:237px;width:116px;height:29px;background:var(--navy);color:var(--white);border-radius:2px;font-size:12px}

/* footer */
.footer-brand{left:198px;top:3416px}
.footer-brand .brand-dot{width:56px;height:56px;background:var(--white)}
.footer-brand .brand-name{color:var(--white);font-size:31px}
.footer-brand .brand-name small{display:block;font-size:17px;letter-spacing:.5px;margin-top:2px}
.footer-about{left:194px;top:3502px;width:270px;font-size:10.5px;line-height:18px;color:#c9d0d8}
.footer-col h5{font-size:12px;font-weight:600;color:var(--white);text-transform:uppercase}
.footer-col .rule{width:155px;height:1px;background:#3a4656;margin-top:8px}
.footer-col ul{list-style:none;margin-top:10px}
.footer-col li{font-size:11px;line-height:21.5px;color:#c9d0d8}
.newsletter-label{font-size:11px;color:#c9d0d8;margin-top:18px}
.newsletter{display:flex;margin-top:8px}
.newsletter .input{width:108px;height:23px;background:var(--white)}
.newsletter .go{width:72px;height:23px;background:var(--navy);color:var(--white);font-size:10px;display:flex;align-items:center;justify-content:center}
.socials{display:flex;gap:7px;margin-top:11px}
.socials span{width:18px;height:18px;border-radius:50%;border:1px solid #c9d0d8}
.footer-rule{left:190px;top:3628px;width:820px;height:1px;background:#2c3847}
.copyright{left:190px;top:3651px;font-size:10px;color:#c9d0d8}
.legal{left:840px;top:3651px;font-size:10px;color:#c9d0d8;word-spacing:4px}
</style>
</head>
<body>

<header class="site-header abs">
  <div class="brand abs"><span class="brand-dot"></span><span class="brand-name">HARLOW<small>SOLUTIONS, LLC</small></span></div>
  <nav class="main-nav abs">
    <a class="active" style="left:0">Home</a>
    <a style="left:71px">About Us</a>
    <a style="left:162px">Services</a>
    <a style="left:248px">Blog</a>
    <a style="left:316px">Contact Us</a>
  </nav>
  <div class="nav-divider abs"></div>
  <div class="phone-pill abs">
    <svg width="14" height="14" viewBox="0 0 24 24"><path fill="#0d4d75" d="M6.6 10.8a15.1 15.1 0 0 0 6.6 6.6l2.2-2.2a1 1 0 0 1 1-.25 11.4 11.4 0 0 0 3.6.57 1 1 0 0 1 1 1V20a1 1 0 0 1-1 1A17 17 0 0 1 3 4a1 1 0 0 1 1-1h3.5a1 1 0 0 1 1 1c0 1.25.2 2.46.57 3.6a1 1 0 0 1-.25 1z"/></svg>
    012 555 0147
  </div>
</header>

<section class="hero">
  <div class="hero-photo abs" role="img" aria-label="Photo of a cheering office team throwing papers in the air"></div>
  <div class="hero-shade abs"></div>
  <svg class="hero-curve abs" viewBox="0 0 1200 130" preserveAspectRatio="none">
    <path d="M0,38 Q600,160 1200,38 L1200,130 L0,130 Z" fill="#ffffff"/>
    <path d="M0,38 Q600,160 1200,38" fill="none" stroke="#8c8c8c" stroke-width="5"/>
  </svg>
  <h1 class="hero-title abs">STAFF AUGMENTATION</h1>
  <p class="hero-sub abs">Businesses often need specialized resources to assist with specific tasks.</p>
  <a class="btn hero-btn abs">Learn More</a>
</section>

<section class="features">
  <article class="feature abs" style="left:224px">
    <svg width="70" height="92" viewBox="0 0 70 92" fill="none" stroke="#0e1722" stroke-width="3">
      <rect x="26" y="4" width="32" height="16" rx="3" fill="#0d4d75" stroke="none"/>
      <circle cx="27" cy="40" r="8"/><circle cx="52" cy="42" r="7"/>
      <path d="M14 64c0-9 6-14 13-14s13 5 13 14"/><path d="M42 64c0-8 4-12 10-12s9 4 9 12v16"/>
      <rect x="6" y="64" width="48" height="8"/><path d="M12 72v18M48 72v18M10 80h40"/>
    </svg>
    <h3>Outsourcing</h3>
    <p>Lorem ipsum dolor amet, consectetur adipiscing elit nullam ac tellus urna Phasellus dictum et purus iaculis.</p>
    <a class="btn">Learn More</a>
  </article>
  <article class="feature is-featured abs" style="left:482px">
    <svg width="70" height="92" viewBox="0 0 70 92" fill="none" stroke="#ffffff" stroke-width="3">
      <path d="M24 14a20 20 0 0 0-12 36c3 3 4 6 4 10h18c0-4 1-7 4-10a20 20 0 0 0-14-36z"/>
      <path d="M16 66h18M18 72h14M21 78h8"/>
      <path d="M40 8l24 14-8 22-18-6" fill="#ffffff" fill-opacity=".15"/>
      <circle cx="24" cy="34" r="6"/>
    </svg>
    <h3>Solutions</h3>
    <p>Lorem ipsum dolor amet, consectetur adipiscing elit nullam ac tellus urna Phasellus dictum et purus iaculis.</p>
    <a class="btn">Learn More</a>
  </article>
  <article class="feature abs" style="left:738px">
    <svg width="92" height="92" viewBox="0 0 92 92" fill="none" stroke="#0e1722" stroke-width="3" style="left:72px">
      <circle cx="16" cy="36" r="11" fill="#0d4d75" stroke="none"/>
      <text x="11" y="42" fill="#ffffff" font-size="16" font-family="Outfit,sans-serif" stroke="none">$</text>
      <circle cx="62" cy="16" r="10" fill="#0d4d75" stroke="none"/>
      <path d="M44 86V50c0-8 8-12 18-12s18 4 18 12v36"/>
      <rect x="6" y="56" width="44" height="30"/>
      <path d="M14 80v-8M22 80v-14M30 80v-10M38 80v-16"/>
    </svg>
    <h3>Managed Service</h3>
    <p>Lorem ipsum dolor amet, consectetur adipiscing elit nullam ac tellus urna Phasellus dictum et purus iaculis.</p>
    <a class="btn">Learn More</a>
  </article>
</section>

<section class="about">
  <h2 class="about-title abs">We know good talent,<br>because we are good talent</h2>
  <p class="about-copy abs">orem Ipsum is simply dummy text of the printing and typesetting industry. Lorem Ipsum has been the industry's standard dummy text ever since the 1500s, when an unknown printer took a galley of type and scrambled it to make a type specimen book. It has survived not only five centuries, but also the leap into electronic typesetting, remaining essentially unchanged.</p>
  <a class="btn about-btn abs">Learn More</a>
  <div class="about-bg abs"></div>
  <div class="about-photo abs" role="img" aria-label="Photo of smiling business team members in office attire"></div>
</section>

<div class="testimonial-bg abs"></div>

<section class="services">
  <svg class="services-band abs" viewBox="0 0 1200 1100" role="img" aria-label="Blue-toned photo of a business handshake behind the services">
    <defs>
      <linearGradient id="bandFill" x1="0" y1="0" x2="1" y2="1">
        <stop offset="0" stop-color="#2b6a90"/><stop offset=".5" stop-color="#3a7aa0"/><stop offset="1" stop-color="#1f5778"/>
      </linearGradient>
    </defs>
    <path d="M0,208 Q600,20 1200,208 L1200,896 Q600,1068 0,896 Z" fill="url(#bandFill)"/>
    <path d="M0,208 Q600,20 1200,208" fill="none" stroke="#8c8c8c" stroke-width="7"/>
    <path d="M0,896 Q600,1068 1200,896" fill="none" stroke="#8c8c8c" stroke-width="7"/>
  </svg>
  <h2 class="services-title abs">Services We Provide</h2>
  <p class="services-sub abs">Our Business strives to lead and coordinate support for a wide range of construction<br>and engineering industries and clients that include</p>

  <article class="service abs" style="left:209px;top:1794px">
    <svg width="62" height="66" viewBox="0 0 62 66" fill="#1f5f8b"><path d="M10 2l-5 8h3v12h4V10h3zM31 2l-5 8h3v12h4V10h3zM52 2l-5 8h3v12h4V10h3z"/><circle cx="10" cy="36" r="6"/><circle cx="52" cy="36" r="6"/><circle cx="31" cy="40" r="6" fill="none" stroke="#1f5f8b" stroke-width="2.5"/><path d="M0 56c0-7 4-11 10-11s10 4 10 11zM42 56c0-7 4-11 10-11s10 4 10 11z"/><path d="M21 64c0-8 4-13 10-13s10 5 10 13z" fill="none" stroke="#1f5f8b" stroke-width="2.5"/></svg>
    <h4>Staff Augmentation</h4>
    <p>Lorem ipsum dolor sit amet, consectetur adipiscing elit nullam ac tellus urna.</p>
  </article>
  <article class="service abs" style="left:478px;top:1794px">
    <svg width="62" height="66" viewBox="0 0 62 66" fill="#1f5f8b"><circle cx="20" cy="10" r="7"/><path d="M10 20h14l6 16h10v6H26l-4-10-4 10 8 10v12h-6V54l-10-12z"/><rect x="28" y="48" width="34" height="4"/><rect x="40" y="6" width="3" height="30"/><rect x="36" y="34" width="12" height="3"/><path d="M56 52v14h-4V52z"/></svg>
    <h4>Screening</h4>
    <p>Lorem ipsum dolor sit amet, consectetur adipiscing elit nullam ac tellus urna.</p>
  </article>
  <article class="service abs" style="left:747px;top:1794px">
    <svg width="62" height="66" viewBox="0 0 62 66" fill="none" stroke="#1f5f8b" stroke-width="2.5"><rect x="4" y="6" width="54" height="54" stroke-dasharray="3 3"/><circle cx="31" cy="33" r="17" fill="#1f5f8b" fill-opacity=".15"/><path d="M14 33h34M31 16v34M19 22c8 4 16 4 24 0M19 44c8-4 16-4 24 0"/><rect x="0" y="2" width="8" height="8" fill="#1f5f8b"/><rect x="54" y="2" width="8" height="8" fill="#1f5f8b"/><rect x="0" y="56" width="8" height="8" fill="#1f5f8b"/><rect x="54" y="56" width="8" height="8" fill="#1f5f8b"/></svg>
    <h4>Sourcing</h4>
    <p>Lorem ipsum dolor sit amet, consectetur adipiscing elit nullam ac tellus urna.</p>
  </article>
  <article class="service abs" style="left:209px;top:2033px">
    <svg width="62" height="66" viewBox="0 0 62 66" fill="#1f5f8b"><path d="M27 4h8l2 7 6 3 7-3 5 6-3 7 2 6 7 2v8l-7 2-2 6 3 7-5 6-7-3-6 3-2 7h-8l-2-7-6-3-7 3-5-6 3-7-2-6-7-2v-8l7-2 2-6-3-7 5-6 7 3 6-3z"/><circle cx="31" cy="32" r="11" fill="#fcefee"/><path d="M22 26l26 30 6-6L28 22z" fill="#0e3e5e"/></svg>
    <h4>Assessing</h4>
    <p>Lorem ipsum dolor sit amet, consectetur adipiscing elit nullam ac tellus urna.</p>
  </article>
  <article class="service abs" style="left:478px;top:2033px">
    <svg width="62" height="66" viewBox="0 0 62 66" fill="#1f5f8b"><path d="M18 14a14 14 0 0 1 26 0" fill="none" stroke="#1f5f8b" stroke-width="2.5"/><path d="M31 20l10 5v11l-10 5-10-5V25z"/><path d="M4 34l8-4 10 18v16H12L4 52zM58 34l-8-4-10 18v16h10l8-12z"/></svg>
    <h4>Dedicated Support</h4>
    <p>Lorem ipsum dolor sit amet, consectetur adipiscing elit nullam ac tellus urna.</p>
  </article>
  <article class="service abs" style="left:747px;top:2033px">
    <svg width="62" height="66" viewBox="0 0 62 66" fill="#1f5f8b"><rect x="2" y="6" width="58" height="42" rx="2"/><rect x="7" y="11" width="48" height="32" fill="#fcefee"/><rect x="26" y="48" width="10" height="10"/><rect x="16" y="58" width="30" height="4"/><circle cx="31" cy="24" r="7"/><path d="M18 40c0-7 6-10 13-10s13 3 13 10z"/></svg>
    <h4>Enquiry</h4>
    <p>Lorem ipsum dolor sit amet, consectetur adipiscing elit nullam ac tellus urna.</p>
  </article>
</section>

<section class="testimonials">
  <blockquote class="quote abs" style="left:219px;top:2565px;width:365px;height:114px">Lorem ipsum dolor sit amet, consectetur adipiscing elit. Nullam ac tellus urna. Phasellus dictum et purus iaculis accumsan. Sed suscipit pharetra.</blockquote>
  <blockquote class="quote abs" style="left:621px;top:2497px;width:361px;height:182px">Lorem ipsum dolor sit amet, consectetur adipiscing elit. Nullam ac tellus urna. Phasellus dictum et purus iaculis accumsan. Sed suscipit pharetra dolor in venenatis. Vivamus eget finibus ipsum, quis placerat sem. Nulla varius erat in libero ornare dignissim. Nam a interdum.</blockquote>

  <div class="avatar abs" style="left:236px;top:2707px" role="img" aria-label="Portrait photo of the client"></div>
  <div class="abs" style="left:296px;top:2714px"><div class="person-name">Maren Holloway, Founder</div><div class="person-role">Westbay Consulting Group</div></div>
  <div class="avatar abs" style="left:638px;top:2707px" role="img" aria-label="Portrait photo of the client"></div>
  <div class="abs" style="left:698px;top:2714px"><div class="person-name">Dario Velasco, Co-Founder</div><div class="person-role">Northfield Labs</div></div>

  <div class="dots abs"><span class="on"></span><span></span><span></span></div>
</section>

<div class="footer-bg abs" role="img" aria-label="Dark mountain landscape at night">
  <svg width="1200" height="502" viewBox="0 0 1200 502" preserveAspectRatio="none">
    <defs><linearGradient id="nightFill" x1="0" y1="0" x2="0" y2="1"><stop offset="0" stop-color="#1a2838"/><stop offset="1" stop-color="#0c1722"/></linearGradient></defs>
    <path d="M0,22 L140,6 L260,30 L400,60 L600,90 L800,60 L940,30 L1060,4 L1200,18 L1200,502 L0,502 Z" fill="url(#nightFill)"/>
  </svg>
</div>

<section class="contact">
  <h2 class="contact-title abs">CONTACT</h2>
  <p class="contact-sub abs">Lorem ipsum dolor sit amet, consectetur adipiscing elit<br>Nunc ac consectetur leo. Mauris aliquam.</p>
  <form class="contact-card abs">
    <h2>Feel Free to Contact Us</h2>
    <div class="field" style="left:90px;top:61px;width:310px;height:29px">First Name</div>
    <div class="field" style="left:413px;top:61px;width:310px;height:29px">Last Name</div>
    <div class="field" style="left:90px;top:104px;width:310px;height:29px">Email</div>
    <div class="field" style="left:413px;top:104px;width:310px;height:29px">Subject</div>
    <div class="field" style="left:90px;top:147px;width:633px;height:75px">Message...</div>
    <span class="btn submit">Submit</span>
  </form>
</section>

<footer>
  <div class="brand footer-brand abs"><span class="brand-dot"></span><span class="brand-name">HARLOW<small>SOLUTIONS, LLC</small></span></div>
  <p class="footer-about abs">Lorem ipsum dolor sit amet, consectetur adipiscing elit. Aenean massa mauris, maximus nec faucibus a, malesuada ut magna. Morbi orci tortor, molestie quis finibus quis, pretium sed diam.</p>
  <div class="footer-col abs" style="left:576px;top:3410px">
    <h5>Sitelinks</h5><div class="rule"></div>
    <ul><li>Home</li><li>About Us</li><li>Services</li><li>Sitemap</li><li>Contact</li></ul>
  </div>
  <div class="footer-col abs" style="left:827px;top:3410px">
    <h5>Stay in Touch</h5>
    <div class="newsletter-label">Subscribe Our Newsletter</div>
    <div class="newsletter"><span class="input"></span><span class="go">Subscribe</span></div>
    <div class="socials"><span></span><span></span><span></span></div>
  </div>
  <div class="footer-rule abs"></div>
  <p class="copyright abs">@ 2022 Harlow Solutions. All Rights Reserved.</p>
  <p class="legal abs">Privace &amp; Policy | Faq | Terms.</p>
</footer>

</body>
</html>
```